Training Program Flyers

***Please note an update - the flyers should have somewhere a space that can include a special offer, which can be removed if not applicable with no impact to the design. Have uploaded a graphic of a current example of an offer**

We require 2 flyers to be re-designed which will include:
- Program Flyer
- Training calendar

Current flyers are attached - which are generally 2 pages long.

Program flyers
The newly designed flyer templates should cater for future use across multiple courses and have space for pictures that will be relevant to the content and also allow for additional content to be added if required (ie the template could be extended to a 3rd page)

Training Calendar
This flyer should be flexible to add additional courses as they arise and extend onto further pages easily.

Our branding guidelines and corporate colours should also be followed as attached.

We require editable files in photoshop/illustrator and PDF
The flyers should be A4 in size

Thank you for your time
Corinne

Target Market(s)

Students paying for services

Industry/Entity Type

Training

Font styles to use
Other font styles liked:
• As per brand guidelines

Requirements
Must have
• Corporate Brand Look and Feel

```html
<!DOCTYPE html>
<html lang="en">
<head>
<meta charset="utf-8">
<title>Training Program Flyer</title>
<link href="https://fonts.googleapis.com/css2?family=Montserrat:wght@600;700;800&family=Open+Sans:wght@400;600;700&display=swap" rel="stylesheet">
<style>
:root{
  --red:#d6262e;
  --red-dark:#b51d24;
  --blue:#2b8fd2;
  --blue-dark:#1f74b0;
  --white:#ffffff;
  --ink:#3a3a3a;
  --photo-a:#c9d6de;
  --photo-b:#e8d9c6;
}
*{margin:0;padding:0;box-sizing:border-box}
html,body{width:900px;height:1200px;overflow:hidden;background:#fff}
body{font-family:"Open Sans",Arial,sans-serif;position:relative}
.flyer{position:absolute;inset:0;width:900px;height:1200px;background:var(--white);overflow:hidden}
.hero-photo{position:absolute;left:0;top:0;width:900px;height:580px;
  background:linear-gradient(120deg,var(--photo-a) 0%,#f1e6d8 45%,var(--photo-b) 70%,#9fb3c2 100%)}
.shapes{position:absolute;left:0;top:0}
.offer{position:absolute;left:50px;top:290px;width:250px;height:130px;background:var(--white);
  border:4px solid var(--blue);padding:12px 16px;color:var(--blue-dark)}
.offer-amount{font-family:"Montserrat",sans-serif;font-weight:800;font-size:30px;color:var(--red);line-height:1}
.offer-title{font-family:"Montserrat",sans-serif;font-weight:700;font-size:18px;margin-top:6px}
.offer-note{font-size:12px;margin-top:4px}
.offer-date{font-family:"Montserrat",sans-serif;font-weight:800;font-size:20px;color:var(--blue-dark)}
.brand{position:absolute;left:520px;top:505px;display:flex;align-items:center;gap:12px}
.brand-dot{width:40px;height:40px;border-radius:50%;background:var(--red)}
.brand-name{font-family:"Montserrat",sans-serif;font-weight:800;font-size:36px;color:var(--red);line-height:1}
.brand-sub{font-family:"Montserrat",sans-serif;font-weight:800;font-size:12px;color:var(--red);letter-spacing:3px;margin-top:4px}
.side{position:absolute;left:0;top:596px;width:360px;height:414px;background:var(--red);padding-top:12px}
.side-head{background:var(--white);color:var(--red);font-family:"Montserrat",sans-serif;font-weight:800;
  font-size:18px;line-height:1.15;padding:8px 24px;margin:0 20px 8px 0}
.side-head.second{margin-top:8px}
.titles{list-style:none;padding:0 24px}
.titles li{background:var(--white);color:var(--red);font-size:12.5px;line-height:1.4;font-weight:600;padding:2px 10px;margin-bottom:4px}
.rules{padding:0 24px;color:var(--white);font-size:13px;line-height:1.4}
.rules p{border-bottom:1px solid rgba(255,255,255,.5);padding:3px 0}
.details{position:absolute;left:0;top:1010px;width:360px;height:190px;background:var(--blue);color:var(--white);padding:14px 24px}
.details-head{font-family:"Montserrat",sans-serif;font-weight:800;font-size:23px;line-height:1.2;margin-bottom:6px}
.details-date{font-family:"Montserrat",sans-serif;font-weight:700;font-size:20px;line-height:1.2}
.details-time{font-family:"Montserrat",sans-serif;font-weight:800;font-size:28px;line-height:1.2;margin-top:4px}
.overview-head{position:absolute;left:400px;top:640px;font-family:"Montserrat",sans-serif;font-weight:800;font-size:34px;color:var(--red)}
.overview{position:absolute;left:400px;top:690px;width:470px;height:290px;background:var(--red);color:var(--white);
  font-size:11.5px;line-height:1.45;padding:16px 20px}
.overview p{margin-bottom:7px}
.entry-head{position:absolute;left:400px;top:1010px;font-family:"Montserrat",sans-serif;font-weight:800;font-size:34px;color:var(--red)}
.entry{position:absolute;left:400px;top:1062px;width:470px;font-size:13px;line-height:1.5;color:var(--ink)}
</style>
</head>
<body>
<div class="flyer">
  <div class="hero-photo" role="img" aria-label="Photo of a smiling student writing at a desk in a classroom"></div>

  <svg class="shapes" width="900" height="640" viewBox="0 0 900 640" aria-hidden="true">
    <polygon points="0,580 0,470 420,450 420,520" fill="var(--blue)"/>
    <polygon points="0,590 900,415 900,640 0,640" fill="var(--white)"/>
    <polygon points="0,576 900,401 900,416 0,591" fill="var(--red)"/>
  </svg>

  <div class="offer">
    <div class="offer-amount">SAVE $100</div>
    <div class="offer-title">Early Bird Special</div>
    <div class="offer-note">Register &amp; pay before</div>
    <div class="offer-date">22nd December</div>
  </div>

  <div class="brand">
    <div class="brand-dot"></div>
    <div>
      <div class="brand-name">Brightpath</div>
      <div class="brand-sub">TRAINING COLLEGE</div>
    </div>
  </div>

  <section class="side">
    <h2 class="side-head">OCCUPATIONAL TITLES<br>MAY INCLUDE</h2>
    <ul class="titles">
      <li>Accommodation support worker</li>
      <li>Hostel supervisor</li>
      <li>Assistant hostel supervisor</li>
      <li>Personal care worker</li>
      <li>Care supervisor</li>
      <li>Care team leader</li>
      <li>Residential care worker</li>
    </ul>
    <h2 class="side-head second">PACKAGING RULES</h2>
    <div class="rules">
      <p>15 units of competency are required for award of this qualification</p>
      <p>10 core units</p>
      <p>5 elective units</p>
    </div>
  </section>

  <section class="details">
    <h2 class="details-head">PROGRAM DETAILS</h2>
    <div class="details-date">17 February 2015<br>to<br>19 April 2016</div>
    <div class="details-time">9.00am – 5.00pm</div>
  </section>

  <h2 class="overview-head">PROGRAM OVERVIEW</h2>
  <section class="overview">
    <p>This accredited program has been designed for existing workers employed within the aged care sector.</p>
    <p>The program will provide you with the skills and knowledge to:<br>
    • carry out activities related to maintaining an individual's well being through personal care and/or other activities of living.<br>
    • provide services to individuals with complex needs, and/or work with groups of older people. Work may include training and support to promote independence and community participation, and programs in a variety of settings including residential and centre-based programs.<br>
    • report to service managers and liaise with professionals and other service providers.<br>
    • supervise and/or coordinate a limited number of other workers.</p>
    <p>This qualification is suitable for people seeking professional or career development in the aged care industry and direct care work.</p>
  </section>

  <h2 class="entry-head">ENTRY REQUIREMENTS</h2>
  <p class="entry">There are no formal entry requirements. However it is recommended that students have basic computer skills, good literacy, numeracy, communication and interpersonal skills. Applicants should have a caring and supportive attitude and be physically fit and able to lift heavy objects and be committed to the rights of elderly people.</p>
</div>
</body>
</html>
```